Business Card for Makeup Artist

I need a business card designed for my makeup and hair artistry business which is primarily events and weddings focused. The card needs to be sleek, simple, stylish and appealing to women. I would prefer a white background but open to suggestions also. I also love the marble background look. I have attached some example pics. It needs to be a double sided card with logo and/or design on one side and contact details in the centre of the card on the other side. NO LOGO ON BACK. Examples attached.

Target Market(s)

Females age 14-55

Industry/Entity Type

Business

Contact Information for Business Card

Nora Pelling
Principal Makeup Artist
P: 0412 903 251
E: nora@lumivamakeup.com.au
W: www.lumivamakeup.com.au

Requirements
Should not have
• No yellow, green, red or blue in the design.

```html
<!DOCTYPE html>
<html lang="en">
<head>
<meta charset="UTF-8">
<title>Lumiva Makeup Artistry – Business Card</title>
<link rel="stylesheet" href="https://fonts.googleapis.com/css2?family=Michroma&family=Questrial&display=swap">
<style>
  :root {
    --page-bg: #e9e9ec;
    --card-white: #ffffff;
    --sparkle-light: #f4f4f6;
    --sparkle-mid: #c9c9cd;
    --sparkle-dark: #9e9ea3;
    --ink: #111111;
    --accent-pink: #df6db4;
    --band-text: #ffffff;
  }
  * { margin: 0; padding: 0; box-sizing: border-box; }
  html, body {
    width: 1200px;
    height: 900px;
    overflow: hidden;
    background: var(--page-bg);
  }
  .canvas {
    width: 1200px;
    height: 900px;
    display: flex;
    flex-direction: column;
    align-items: center;
    justify-content: center;
    gap: 40px;
  }
  .card {
    position: relative;
    width: 680px;
    height: 388px;
    border-radius: 22px;
    overflow: hidden;
    background: var(--card-white);
    box-shadow: 0 10px 28px rgba(0, 0, 0, 0.18);
  }
  .sparkle-field {
    position: absolute;
    inset: 0;
    background:
      radial-gradient(ellipse at 30% 30%, var(--sparkle-light) 0%, transparent 55%),
      radial-gradient(ellipse at 75% 65%, var(--sparkle-light) 0%, transparent 50%),
      linear-gradient(135deg, var(--sparkle-mid) 0%, var(--sparkle-light) 45%, var(--sparkle-dark) 100%);
  }

  /* Front */
  .brand {
    position: absolute;
    left: 50%;
    top: 50%;
    transform: translate(-50%, -50%);
    display: flex;
    align-items: center;
    gap: 18px;
  }
  .brand-dot {
    width: 22px;
    height: 22px;
    border-radius: 50%;
    background: var(--accent-pink);
  }
  .brand-name {
    font-family: "Questrial", sans-serif;
    font-size: 46px;
    line-height: 1.05;
    color: var(--ink);
    letter-spacing: 2px;
    text-transform: uppercase;
  }
  .brand-name span { display: block; font-size: 24px; letter-spacing: 5px; }

  /* Back */
  .contact-band {
    position: absolute;
    inset: 0;
  }
  .holder {
    position: absolute;
    left: 300px;
    top: 206px;
  }
  .holder-name {
    font-family: "Michroma", sans-serif;
    font-size: 22px;
    color: var(--ink);
    letter-spacing: 1px;
    text-transform: uppercase;
  }
  .holder-title {
    font-family: "Questrial", sans-serif;
    font-size: 15px;
    color: var(--accent-pink);
    margin-top: 2px;
    padding-left: 30px;
  }
  .contact-list {
    position: absolute;
    left: 400px;
    top: 286px;
    list-style: none;
    font-family: "Questrial", sans-serif;
    font-size: 14px;
    line-height: 21px;
    color: var(--band-text);
  }
  .contact-list b {
    display: inline-block;
    width: 24px;
    font-weight: normal;
  }
</style>
</head>
<body>
<main class="canvas">

  <section class="card card-front" aria-label="Card front">
    <div class="sparkle-field" role="img" aria-label="Soft silver and white bokeh sparkle background"></div>
    <div class="brand">
      <span class="brand-dot"></span>
      <div class="brand-name">Lumiva<span>Makeup Artistry</span></div>
    </div>
  </section>

  <section class="card card-back" aria-label="Card back">
    <div class="sparkle-field" role="img" aria-label="Soft silver and white bokeh sparkle background"></div>
    <svg class="contact-band" viewBox="0 0 680 388" width="680" height="388" aria-hidden="true">
      <path d="M0,388 Q420,368 680,140" fill="none" stroke="#1a1a1a" stroke-width="5"/>
      <path d="M0,392 Q420,372 680,144 L680,388 Z" fill="var(--accent-pink)"/>
    </svg>
    <div class="holder">
      <p class="holder-name">Nora Pelling</p>
      <p class="holder-title">Principal Makeup Artist</p>
    </div>
    <ul class="contact-list">
      <li><b>P:</b>0412 903 251</li>
      <li><b>E:</b>nora@lumivamakeup.com.au</li>
      <li><b>W:</b>www.lumivamakeup.com.au</li>
    </ul>
  </section>

</main>
</body>
</html>
```